Tolvik cards

I want a simple business card that pops.
Logo on one side.
On side two i want.
"Are you thinking about a new building on your property, or renovating an existing structure? Contact".....
Owners Name: Gary Pellman
Owners Phone number: 555-209-4176
Address:4716 Copper Fern RD, Harlan Ridge, PA 15590
Committed to Quality, Service, and Integrity

```html
<!DOCTYPE html>
<html lang="en">
<head>
<meta charset="utf-8">
<title>Tolvik Builders LLC – Business Card</title>
<link href="https://fonts.googleapis.com/css2?family=Montserrat:wght@400;500;700&display=swap" rel="stylesheet">
<style>
  :root {
    --backdrop: #9a9a9a;
    --card-dark: #151515;
    --card-dark-sheen: #262626;
    --card-light: #ffffff;
    --ink: #2e2e2e;
    --brand-brown: #5a4230;
    --band-brown: #3f2c1d;
    --on-dark: #ffffff;
  }
  * { box-sizing: border-box; margin: 0; padding: 0; }
  html, body {
    width: 1200px; height: 1108px; overflow: hidden;
    background: var(--backdrop);
    font-family: "Montserrat", Arial, sans-serif;
  }
  .canvas { position: relative; width: 1200px; height: 1108px; }

  .card {
    position: absolute; left: 242px; width: 715px; height: 409px;
    border-radius: 29px; overflow: hidden;
  }
  .card--front {
    top: 119px;
    background: linear-gradient(120deg, var(--card-dark) 0%, var(--card-dark) 42%, var(--card-dark-sheen) 55%, var(--card-dark) 72%, var(--card-dark) 100%);
  }
  .front-brand {
    position: absolute; left: 88px; top: 140px;
    display: flex; align-items: center; gap: 26px;
    color: var(--on-dark); font-weight: 700;
  }
  .front-brand__mark { width: 96px; height: 96px; background: var(--on-dark); }
  .front-brand__name { font-size: 86px; line-height: 0.9; letter-spacing: 0; }
  .front-brand__name small { display: block; font-size: 29px; letter-spacing: 2px; margin-top: 8px; }

  .card--back { top: 580px; height: 408px; background: var(--card-light); }
  .back-intro {
    position: absolute; top: 19px; left: 0; right: 0;
    text-align: center; color: var(--ink);
    font-size: 18px; line-height: 29px; letter-spacing: .4px;
  }
  .back-brand {
    position: absolute; left: 44px; top: 116px; width: 296px; height: 180px;
    display: flex; flex-direction: column; align-items: center; justify-content: flex-end;
    color: var(--brand-brown); font-weight: 700; text-align: center;
  }
  .back-brand__name { font-size: 58px; line-height: 0.9; letter-spacing: 0; }
  .back-brand__name small { display: block; font-size: 19px; letter-spacing: 1.5px; margin-top: 6px; }
  .back-divider {
    position: absolute; left: 348px; top: 116px; width: 2px; height: 176px;
    background: var(--brand-brown);
  }
  .contact { position: absolute; left: 385px; top: 110px; color: var(--ink); }
  .contact__name { font-size: 33px; font-weight: 700; color: var(--brand-brown); letter-spacing: .3px; line-height: 40px; }
  .contact__role { font-size: 18px; line-height: 22px; letter-spacing: .6px; margin-top: 4px; }
  .contact__address { font-size: 18px; line-height: 29px; letter-spacing: .4px; margin-top: 20px; }
  .contact__phone { display: flex; align-items: center; gap: 8px; font-size: 18px; line-height: 22px; letter-spacing: .4px; margin-top: 21px; }
  .contact__phone svg { width: 17px; height: 13px; fill: var(--ink); }
  .tagline-band {
    position: absolute; left: 0; right: 0; top: 359px; height: 25px;
    background: var(--band-brown); color: var(--on-dark);
    text-align: center; font-size: 17px; line-height: 25px; letter-spacing: .5px;
  }
</style>
</head>
<body>
<main class="canvas">
  <section class="card card--front" aria-label="Card front">
    <div class="front-brand">
      <span class="front-brand__mark"></span>
      <div class="front-brand__name">TOLVIK<small>BUILDERS LLC</small></div>
    </div>
  </section>

  <section class="card card--back" aria-label="Card back">
    <p class="back-intro">Are you thinking about a new building on your<br>property, or renovating an existing structure? Contact</p>

    <div class="back-brand">
      <div class="back-brand__name">TOLVIK<small>BUILDERS LLC</small></div>
    </div>

    <div class="back-divider"></div>

    <div class="contact">
      <h1 class="contact__name">Gary Pellman</h1>
      <p class="contact__role">Owner</p>
      <p class="contact__address">4716 Copper Fern RD,<br>Harlan Ridge, PA 15590</p>
      <p class="contact__phone">
        <svg viewBox="0 0 17 13" aria-hidden="true"><path d="M1 4C1 1.5 4 .5 8.5.5S16 1.5 16 4v1h-4V3.5H5V5H1z"/><path d="M4 6h9l2.5 6.5h-14z"/></svg>
        555-209-4176
      </p>
    </div>

    <div class="tagline-band">Committed to Quality, Service, and Integrity</div>
  </section>
</main>
</body>
</html>
```